An expert for Professional and Technical Evaluation of Painting Work Needs a New Letterhead Design

I own a mid-sized painting company and also work as an expert for professional and technical evaluation of painting work in the area of Zurich.

Please read the project description and the must-have-requirements carefully!

I attached 1 PDF which will help you create a new letterhead design:

THE NEW DESIGN DOESN'T NEED A LOGO! (Because it won't represent a company, it represents only a service)
Updates

Dear designers We had a discussion about the location/placement of the design and came to the conclusion that we only want the design to be in the header area of the A4-paper. We would be glad to receive some revised version of your designs. Thank you and kind regards!

Reason: Due to the fact that only 20% of the designer have understood the brief and submitted designs that have met the requirements we decided to extend the contest deadline.

Reason: A great deal of good designs were submitted in the last few days. A big thank you to all the participating designers for your good work. We need a few more days to discuss some changes with certain designers and to decide which design will win.

Target Market(s)

(Insurance) Companies, partly also private clients.

Industry/Entity Type

Painting

Colors

Designer to choose colors to be used in the design.

Requirements
Must have
• All information (text, phone numbers, ...) of the old design ("old_letterhead_design.pdf") has also to be in the new one. Additional to that there are a few changes:
The phone numbers "01 583 61 47" and "01 583 61 37" change to "044 583 61 47" and "044 583 61 37". And please mention also this email address: gutachten@holvantrek.example .

- The design should only be in the header-area of the A4-paper. An the background color of the A4-paper will be white.

- The design should consist of two designs. One for the first page and a smaller version of the design for the following pages.

- THE NEW DESIGN DOESN'T NEED A LOGO! You can make a design with geometric forms, ...

- The new design should have a juridical look. It should only contain colors like brown, fawn, black, light green, ...... colors which look serious/reliable.
Nice to have
• Geometric Forms, Symbols or other design elements.

- It would also be nice to have some design elements which emphasize the kind of work we are offering.

```html
<!DOCTYPE html>
<html lang="de">
<head>
<meta charset="utf-8">
<title>Letterhead – Rolf Amsler</title>
<link rel="stylesheet" href="https://fonts.googleapis.com/css2?family=Didact+Gothic&family=Arimo:wght@400;700&display=swap">
<style>
  :root {
    --green-deep: #2fb04a;
    --green-mid: #5cbf3c;
    --green-light: #8cc63f;
    --ink: #111111;
    --paper: #ffffff;
  }
  * { margin: 0; padding: 0; box-sizing: border-box; }
  html, body { width: 900px; height: 1200px; overflow: hidden; background: var(--paper); }
  .page {
    position: relative;
    width: 900px;
    height: 1200px;
    background: var(--paper);
    font-family: "Arimo", Arial, sans-serif;
    color: var(--ink);
    overflow: hidden;
  }
  .honeycomb-header {
    position: absolute;
    left: 0; top: 0;
    width: 362px; height: 245px;
  }
  .sender {
    position: absolute;
    right: 33px; top: 25px;
    text-align: right;
    font-family: "Didact Gothic", "Century Gothic", sans-serif;
    font-size: 16px;
    line-height: 27.5px;
  }
  .sender-name {
    font-size: 27px;
    line-height: 36px;
    color: var(--green-deep);
    letter-spacing: 0.3px;
  }
  .sender-address span + span { margin-left: 30px; }
  .services {
    position: absolute;
    left: 134px; right: 33px; top: 211px;
    display: flex;
    justify-content: space-between;
    list-style: none;
    padding-bottom: 5px;
    border-bottom: 1.5px solid var(--green-mid);
    font-size: 15px;
    line-height: 18px;
    font-weight: 700;
  }
  .services li { display: flex; align-items: center; }
  .services li::before {
    content: "";
    width: 9px; height: 9px;
    background: var(--green-deep);
    margin-right: 8px;
  }
  .letter-body {
    position: absolute;
    left: 52px; right: 47px; top: 292px;
    font-size: 18px;
    line-height: 21.2px;
    text-align: justify;
  }
  .letter-body h1 {
    font-size: 23px;
    line-height: 28px;
    font-weight: 400;
    margin-bottom: 12px;
  }
  .letter-body p { margin-bottom: 21.2px; }
  .letter-body p.tight { margin-bottom: 0; }
</style>
</head>
<body>
<main class="page">
  <svg class="honeycomb-header" viewBox="0 0 362 245" role="img" aria-label="Honeycomb pattern of green hexagons fading from deep to light green">
    <defs>
      <linearGradient id="header-green" x1="0" y1="0" x2="0.35" y2="1">
        <stop offset="0" stop-color="#2fb04a"/>
        <stop offset="1" stop-color="#8cc63f"/>
      </linearGradient>
    </defs>
    <path d="M0 0 H362 L352 42 L302 62 L252 94 L232 146 L176 172 L120 156 L90 198 L45 245 H0 Z" fill="url(#header-green)"/>
  </svg>

  <header class="sender">
    <div class="sender-name">Rolf Amsler</div>
    <div class="sender-address"><span>Eidg.dipl.Malermeister</span><span>Seerain 4</span><span>8816 Hirzel</span></div>
    <div>Telefon : 044 583 61 47</div>
    <div>Fax : 044 583 61 37</div>
    <div>Natel : 079 512 40 26</div>
    <div>Email : gutachten@holvantrek.example</div>
  </header>

  <ul class="services">
    <li>Gutachten</li>
    <li>Expertisen</li>
    <li>Devisierungen</li>
    <li>Farbberatungen</li>
    <li>Dekorative Gestaltungen</li>
  </ul>

  <article class="letter-body">
    <h1>Sample Text</h1>
    <p>Design is the creation of a plan or convention for the construction of an object or a system (as in architectural blueprints, engineering drawings, business processes, circuit diagrams and sewing patterns).[1] Design has different connotations in different fields (see design disci&shy;plines below). In some cases the direct construction of an object (as in pottery, engineering, management, cowboy coding and graphic design) is also considered to be design.</p>
    <p>More formally design has been defined as follows.</p>
    <p class="tight">(noun) a specification of an object, manifested by an agent, intended to accomplish goals, in a particular environment, using a set of primitive components, satisfying a set of require&shy;ments, subject to constraints;</p>
    <p class="tight">(verb, transitive) to create a design, in an environment (where the designer operates)[2]</p>
    <p>Another definition for design is a roadmap or a strategic approach for someone to achieve a unique expectation. It defines the specifications, plans, parameters, costs, activities, pro&shy;cesses and how and what to do within legal, political, social, environmental, safety and economic constraints in achieving that objective.[3]</p>
    <p>Here, a "specification" can be manifested as either a plan or a finished product, and "primi&shy;tives" are the elements from which the design object is composed.</p>
    <p>With such a broad denotation, there is no universal language or unifying institution for design&shy;ers of all disciplines. This allows for many differing philosophies and approaches toward the subject (see Philosophies and studies of design, below).</p>
    <p>The person designing is called a designer, which is also a term used for people who work pro&shy;fessionally in one of the various design areas, usually also specifying which area is being dealt with (such as a fashion designer, concept designer or web designer). A designer's sequence of activities is called a design process. The scientific study of design is called design science.[4][5][6][7]</p>
    <p>Designing often necessitates considering the aesthetic, functional, economic and sociopoliti&shy;cal dimensions of both the design object and design process. It may involve considerable research, thought, modeling, interactive adjustment, and re-design. Meanwhile, diverse kinds of objects may be designed, including clothing, graphical user interfaces, skyscrapers, corpo&shy;rate identities, business processes and even methods of designing</p>
  </article>
</main>
</body>
</html>
```